Product flyer with pricing

We manufacture iconic and luxury vending trailers. for our first trailer we need a flyer created to give to prospective clients with base pricing. I am uploading an example along with graphic files.

```html
<!DOCTYPE html>
<html lang="en">
<head>
<meta charset="utf-8">
<title>Soft Field House Mini – Bright Nook Builds</title>
<link href="https://fonts.googleapis.com/css2?family=Fira+Sans+Condensed:wght@700&family=Fira+Sans:wght@400;500&family=Montserrat:wght@800&family=Varela+Round&display=swap" rel="stylesheet">
<style>
  :root{
    --orange:#e8731a;
    --orange-hot:#e9571b;
    --gold:#f3b21c;
    --yellow:#f3c61b;
    --green:#3f8f2f;
    --green-deep:#3a7a28;
    --slate:#3d4047;
    --steel:#a9abae;
    --silver:#c6c7c9;
    --white:#ffffff;
  }
  *{margin:0;padding:0;box-sizing:border-box}
  html,body{width:848px;height:1200px;overflow:hidden;background:var(--white)}
  .flyer{position:relative;width:1000px;height:1415px;transform:scale(.848);transform-origin:0 0;background:var(--white);font-family:"Varela Round",sans-serif;overflow:hidden}
  .shapes{position:absolute;inset:0;width:1000px;height:1415px}
  .abs{position:absolute}

  .brand{left:140px;top:120px;width:270px;display:flex;align-items:center;justify-content:center;gap:12px}
  .brand-dot{width:26px;height:26px;border-radius:50%;background:var(--gold);flex:none}
  .brand-name{font-family:"Montserrat",sans-serif;font-weight:800;font-size:27px;color:var(--green);line-height:1.05;text-transform:uppercase;letter-spacing:.5px}

  .hero-the{left:0;width:570px;top:256px;text-align:center;font-family:"Fira Sans Condensed",sans-serif;font-weight:700;font-size:44px;color:var(--white)}
  .hero-title{left:0;width:570px;top:316px;text-align:center;font-family:"Fira Sans Condensed",sans-serif;font-weight:700;font-size:80px;line-height:82px;color:var(--white)}
  .hero-sub{left:38px;top:496px;font-family:"Fira Sans",sans-serif;font-size:31px;color:var(--white);letter-spacing:.3px}

  .features-head{left:38px;top:590px;font-family:"Montserrat",sans-serif;font-weight:800;font-size:34px;line-height:38px;color:var(--green);letter-spacing:1px}
  .price{left:278px;top:612px;font-family:"Fira Sans",sans-serif;font-weight:500;font-size:28px;color:var(--white)}
  .price strong{font-family:"Montserrat",sans-serif;font-weight:800;font-size:32px;color:var(--orange-hot)}

  .features{left:112px;top:676px;width:780px;list-style:none;color:var(--yellow);font-size:20px;line-height:24px}
  .features li{position:relative;padding-left:23px}
  .features li::before,.options li::before{content:"";position:absolute;left:0;top:7px;width:11px;height:11px;border-radius:50%;background:var(--yellow)}
  .features .indent{display:block;padding-left:162px}

  .uses-head{left:44px;top:874px;font-family:"Montserrat",sans-serif;font-weight:800;font-size:31px;color:var(--yellow)}
  .options-head{left:440px;top:872px;font-family:"Montserrat",sans-serif;font-weight:800;font-size:35px;color:var(--green);letter-spacing:.5px}

  .uses{left:38px;top:922px;width:318px;color:var(--white);font-size:14.5px;line-height:20.5px}
  .uses span{color:var(--yellow)}

  .options{left:366px;top:928px;width:630px;list-style:none;color:var(--white);font-size:20px;line-height:23.4px}
  .options li{position:relative;padding-left:17px}
  .options li::before{top:6px;width:10px;height:10px}
  .options b{font-weight:400;color:var(--yellow)}

  .contact{top:1330px;color:var(--white);font-family:"Fira Sans",sans-serif;font-size:25px;line-height:34px;white-space:nowrap}
  .contact-address{left:108px}
  .contact-phone{left:428px;width:180px;text-align:center}
  .contact-web{left:774px}
</style>
</head>
<body>
<main class="flyer">
  <svg class="shapes" viewBox="0 0 1000 1415">
    <defs>
      <linearGradient id="band" x1="0" y1="0" x2="1" y2="0.35">
        <stop offset="0" stop-color="#f2bd1e"/>
        <stop offset="1" stop-color="#e6701a"/>
      </linearGradient>
      <linearGradient id="scene" x1="0" y1="0" x2="0" y2="1">
        <stop offset="0" stop-color="#2f6fd6"/>
        <stop offset=".45" stop-color="#dfe3e6"/>
        <stop offset=".75" stop-color="#8a8173"/>
        <stop offset="1" stop-color="#3d3f44"/>
      </linearGradient>
      <linearGradient id="thumb" x1="0" y1="0" x2="0" y2="1">
        <stop offset="0" stop-color="#4a7fcf"/>
        <stop offset=".5" stop-color="#e8e9ea"/>
        <stop offset="1" stop-color="#3f4246"/>
      </linearGradient>
    </defs>
    <rect class="panel-dark" x="0" y="575" width="1000" height="750" fill="var(--slate)"/>
    <polygon class="hero-band" points="0,220 610,220 505,345 640,575 0,575" fill="url(#band)"/>
    <polygon class="frame-steel" points="655,20 1000,20 1000,662 655,662 497,345" fill="var(--steel)"/>
    <polygon class="frame-orange" points="680,40 1000,40 1000,645 680,645 518,345" fill="url(#band)"/>
    <polygon class="price-tag" points="263,598 622,598 650,662 263,662" fill="var(--silver)"/>
    <polygon class="hero-photo" role="img" aria-label="Photo of the white board-and-batten vending house on its trailer, front door and serving window, under blue sky" points="700,60 1000,60 1000,625 700,625 545,345" fill="url(#scene)"/>

    <rect class="gallery-photo" role="img" aria-label="Side view of the vending house hitched to a pickup truck" x="0" y="1093" width="338" height="223" fill="url(#thumb)"/>
    <rect class="gallery-photo" role="img" aria-label="Man opening the gas-shock serving window of the vending house" x="352" y="1093" width="298" height="223" fill="url(#thumb)"/>
    <rect class="gallery-photo" role="img" aria-label="Rear three-quarter view of the vending house on tandem wheels" x="665" y="1093" width="335" height="223" fill="url(#thumb)"/>

    <rect class="footer" x="0" y="1325" width="1000" height="90" fill="var(--green-deep)"/>
    <g class="icon-pin" fill="none" stroke="#fff" stroke-width="4">
      <path d="M68 1387 C52 1367 46 1358 46 1346 a22 22 0 0 1 44 0 c0 12 -6 21 -22 41z"/>
      <circle cx="68" cy="1346" r="8"/>
    </g>
    <path class="icon-phone" fill="#fff" transform="translate(-14 0)" d="M398 1333 l8 0 4 16 -7 5 c2 8 5 14 10 19 l6 -5 12 9 -4 9 c-14 2 -30 -20 -34 -38z"/>
    <g class="icon-mail" fill="none" stroke="#fff" stroke-width="4">
      <rect x="704" y="1344" width="50" height="36"/>
      <path d="M704 1344 l25 20 25 -20 M704 1380 l18 -17 M754 1380 l-18 -17"/>
    </g>
  </svg>

  <div class="abs brand"><span class="brand-dot"></span><span class="brand-name">Bright Nook<br>Builds</span></div>

  <div class="abs hero-the">THE</div>
  <h1 class="abs hero-title">SOFT FIELD<br>HOUSE MINI</h1>
  <p class="abs hero-sub">LUXURY, MOBILE VENDING HOUSE</p>

  <h2 class="abs features-head">BASE UNIT<br>FEATURES</h2>
  <p class="abs price">BASE PRICE: <strong>$45,000</strong></p>

  <ul class="abs features">
    <li>Trailer features tandem wheels w/ brakes.</li>
    <li>Steel frame construction for fire retardation safety and weight reduction.</li>
    <li>100% off grid with solar and lithium battery system allowing the trailer<span class="indent">to be used in places not accessible by traditional trailers.</span></li>
    <li>80 gallon water supply tank.</li>
    <li>100 gallon waste water tank.</li>
    <li>Cupboards, cabinets &amp; four stainless steel sinks.</li>
    <li>60” Gas shock serving window.</li>
  </ul>

  <h2 class="abs uses-head">USE CASES:</h2>
  <h2 class="abs options-head">AVAILABLE OPTIONS:</h2>

  <p class="abs uses">
    <span>Food:</span> Lemonade, Coffee, pizza, cookies,<br>doughnuts, barbecue and more!<br>
    <span>Retail:</span> Clothing, watches, jewelry,<br>flowers and more!<br>
    <span>Corporate:</span> Product info, demonstration,<br>information, brand awareness.<br>
    <span>Fundraisers:</span> Girls / boy sports, non profits, etc.
  </p>

  <ul class="abs options">
    <li>HVAC - Northwind Mini Split - <b>$1,800</b></li>
    <li>Cooler / Glass front Commercial refrigerator - <b>$1,600</b></li>
    <li>Upper loft storage area - <b>$1,200</b></li>
    <li>Signage and graphics - <b>$2,000-$5,000</b> depend on complexity</li>
    <li>Ice machine - <b>$1,100</b></li>
    <li>Other custom items available on request.</li>
  </ul>

  <p class="abs contact contact-address">123, Main Street,<br>Your City, USA</p>
  <p class="abs contact contact-phone">For Booking<br>+1 555 014 2290</p>
  <p class="abs contact contact-web">hi@brightnook.co<br>www.brightnook.co</p>
</main>
</body>
</html>
```